TARO PTY LTD - Business Cards

Design a modern business card - using the attached Designs.
Same design as on the front, apart from the names/numbers/emails to be different.
We want the cards to be very glossy to stand out, do I think the simple black/white/metallic will be effective.
Both lots of details below:

Lyle Marrick
Director
lyle_taro@quintmail.example
0493 628 304

Simon Prowle
Director
simon_taro@quintmail.example
0438 514 209

```html
<!DOCTYPE html>
<html lang="en">
<head>
<meta charset="utf-8">
<title>TARO PTY LTD – Business Cards</title>
<link rel="stylesheet" href="https://fonts.googleapis.com/css2?family=Lato:wght@400;700;900&display=swap">
<style>
  :root {
    --backdrop: #3a3a3c;
    --card: #ffffff;
    --ink: #111111;
    --band: #0b0b0b;
    --metal: #8d8f93;
    --metal-light: #c9cbce;
  }
  * { box-sizing: border-box; margin: 0; padding: 0; }
  html, body {
    width: 1200px; height: 926px; overflow: hidden;
    background: var(--backdrop);
    font-family: "Lato", Arial, sans-serif;
    color: var(--ink);
  }
  .sheet {
    width: 1200px; height: 926px;
    display: flex; flex-direction: column; align-items: center; justify-content: center;
    gap: 60px;
  }
  .card {
    position: relative;
    width: 700px; height: 400px;
    background: var(--card);
    overflow: hidden;
    box-shadow: 0 14px 30px rgba(0,0,0,.35);
  }
  .card__band { position: absolute; left: 0; bottom: 0; width: 100%; height: 100%; }
  .card__details {
    position: absolute; left: 170px; top: 62px;
  }
  .card__role {
    display: inline-block;
    font-size: 15px; letter-spacing: 2.5px;
    border-bottom: 2px solid var(--ink);
    padding-bottom: 1px; margin-right: 6px;
    vertical-align: 4px;
  }
  .card__name {
    display: inline;
    font-size: 34px; font-weight: 400; letter-spacing: 1.5px; text-transform: uppercase;
  }
  .card__name strong { font-weight: 700; }
  .card__contact {
    margin: 10px 0 0 70px;
    font-size: 19px; letter-spacing: 1px; line-height: 1.35;
  }
  .card__contact b { font-weight: 700; }
  .card__mark {
    position: absolute; left: 50%; top: 222px; transform: translateX(-50%);
    display: flex; align-items: center; gap: 14px;
  }
  .card__mark-dot {
    width: 66px; height: 66px; border-radius: 50%;
    background: var(--metal);
  }
  .card__mark-name {
    font-size: 46px; font-weight: 900; letter-spacing: 4px; color: var(--metal);
  }
</style>
</head>
<body>
<main class="sheet">
  <article class="card">
    <svg class="card__band" viewBox="0 0 700 400" preserveAspectRatio="none" aria-hidden="true">
      <path d="M0 300 Q 360 440 700 330 L700 400 L0 400 Z" fill="var(--band)"/>
    </svg>
    <div class="card__details">
      <span class="card__role">DIRECTOR</span>
      <h2 class="card__name">Lyle <strong>Marrick</strong></h2>
      <p class="card__contact"><b>PHONE:</b> 0493 628 304<br><b>EMAIL:</b> lyle_taro@quintmail.example</p>
    </div>
    <div class="card__mark">
      <span class="card__mark-dot"></span>
      <span class="card__mark-name">TARO</span>
    </div>
  </article>

  <article class="card">
    <svg class="card__band" viewBox="0 0 700 400" preserveAspectRatio="none" aria-hidden="true">
      <path d="M0 300 Q 360 440 700 330 L700 400 L0 400 Z" fill="var(--band)"/>
    </svg>
    <div class="card__details">
      <span class="card__role">DIRECTOR</span>
      <h2 class="card__name">Simon <strong>Prowle</strong></h2>
      <p class="card__contact"><b>PHONE:</b> 0438 514 209<br><b>EMAIL:</b> simon_taro@quintmail.example</p>
    </div>
    <div class="card__mark">
      <span class="card__mark-dot"></span>
      <span class="card__mark-name">TARO</span>
    </div>
  </article>
</main>
</body>
</html>
```